Header for Academic Handouts (How-to-Guides)

We are looking for a design element, which can be used as a visual header on A4-word-documents (Portrait-Set-Up). It shall be a graphic, visual language which is clearly understandable. The header height shall be between 0.75 - 1.5 inch – so it should not have too many small details. Attached below ideas/directions how the final document could look like.

The visual element shall symbolize by simple means the topic of “flipped classroom” or “active learning”. The documents with these new graphic elements will be used on handouts which are distributed in this training course:
https://www.kolvabrun.ch/en/the-kolvabrun-hochschule/education/educational-development/didaktische-weiterbildung/flipped-classroom.html

```html
<!DOCTYPE html>
<html lang="en">
<head>
<meta charset="utf-8">
<title>Flipped Classroom – Handout Header</title>
<link rel="stylesheet" href="https://fonts.googleapis.com/css2?family=Roboto+Condensed:wght@700&display=swap">
<style>
  :root {
    --canvas-bg: #ffffff;
    --band-grey: #c9c6c6;
    --brand-blue: #1c57a8;
    --icon-blue: #4f80d6;
    --label-white: #ffffff;
    --shadow: rgba(0, 0, 0, 0.45);
  }
  html, body {
    margin: 0;
    padding: 0;
    width: 1200px;
    height: 526px;
    overflow: hidden;
    background: var(--canvas-bg);
  }
  .header-graphic {
    display: block;
    width: 1200px;
    height: 526px;
  }
  .header-band { fill: var(--band-grey); }
  .title-plate { fill: var(--brand-blue); filter: url(#plate-shadow); }
  .screen-icon { fill: none; stroke: var(--icon-blue); stroke-width: 2.4; stroke-linejoin: round; }
  .title-word {
    font-family: "Roboto Condensed", "Arial Narrow", sans-serif;
    font-weight: 700;
    font-size: 56px;
  }
  .title-word--flipped { fill: var(--brand-blue); }
  .title-word--classroom { fill: var(--label-white); }
</style>
</head>
<body>
<svg class="header-graphic" viewBox="0 0 1200 526" xmlns="http://www.w3.org/2000/svg" role="img" aria-label="Flipped Classroom header">
  <defs>
    <filter id="plate-shadow" x="-5%" y="-10%" width="115%" height="130%">
      <feDropShadow dx="4" dy="4" stdDeviation="2.5" flood-color="#000" flood-opacity="0.45"/>
    </filter>
  </defs>

  <rect class="header-band" x="29" y="154" width="1144" height="148"/>

  <polygon class="title-plate" points="514,152 1147,152 1147,292 572,292"/>

  <g class="screen-icon" transform="translate(250 205)">
    <rect x="0" y="0" width="96" height="58" rx="4"/>
    <rect x="5" y="5" width="86" height="48" rx="2"/>
    <rect x="10" y="10" width="76" height="38" rx="1"/>
    <path d="M40 58 L40 67 M56 58 L56 67"/>
    <rect x="32" y="67" width="32" height="6" rx="2"/>
  </g>

  <text class="title-word title-word--flipped" x="367" y="261" textLength="173" lengthAdjust="spacingAndGlyphs">FLIPPED</text>
  <text class="title-word title-word--classroom" x="568" y="261" textLength="266" lengthAdjust="spacingAndGlyphs">CLASSROOM</text>
</svg>
</body>
</html>
```